Stationery Design

Need a stationery design for an established accounting firm based in London, England.

The company’s name is ‘Marcus Fenwell’. We provide a broad range of bookkeeping, accounting, audit, tax and business services to a wide range of clients (ie, individuals, company, partnerships, etc).

The stationary design needs to show strength and trust and should be clean, corporate and professional.

Only 2 colours must be used as noted on the logo.

The fonts are in Optima

We need the following:

#1: Business Cards (design on 2 sides)
#2: Letterhead (word format) and can be sent to printers
#3: Continuation sheets (word format) and can be sent to printers
#4: Sales invoice template (word format) and can be sent to printers
#5: Report Cover front and back for binding,
#6: Complimentary Slips,
#7: Legal corners with our logo only
#7: Email signature templates

I have attached my company's logo in various file formats

We also need to have our accountancy association’s logo and this must be in the same colour as the dark blue. This BRTQ logo must be at least 8mm square (can be larger). I have attached the BRTQ logo in various file formats

I have also attached other information that you will need for the letter head and invoice templates

I have also attached our old letterhead, fee note template for reference
Updates

Dear Designers - I have increased the budget

Dear Designers - I have read your comments on the fact that the prize does not reflect the work. Thank you and I appreciate your comments. Unfortunately, I am a start up and my budget is limited. As an Alternative, I have reduced the work that I am asking for to the following items and I hope you can assist: #1: Business Cards (design on 2 sides) #2: Letterhead (word format) and can be sent to printers #3: Report Cover front and back for binding, #4: Email signature templates Regards

Reason: I have reduced the work to be done and hence want to capture more designers.

Industry/Entity Type

Accounting

```html
<!DOCTYPE html>
<html lang="en">
<head>
<meta charset="utf-8">
<title>Marcus Fenwell Accountants – Stationery</title>
<link rel="stylesheet" href="https://fonts.googleapis.com/css2?family=Tenor+Sans&display=swap">
<style>
  :root {
    --navy: #1d3a6b;
    --plum: #8e2f8a;
    --paper: #ffffff;
    --backdrop: #ebe8e3;
    --envelope-edge: #d3d3d3;
  }
  html, body {
    margin: 0;
    padding: 0;
    overflow: hidden;
  }
  body {
    width: 1200px;
    height: 806px;
    position: relative;
    background: var(--backdrop);
    font-family: "Tenor Sans", "Optima", sans-serif;
    color: var(--navy);
  }
  .sheet {
    position: absolute;
    background: var(--paper);
    box-shadow: 0 1px 4px rgba(0,0,0,0.12);
  }

  /* Wordmark */
  .wordmark {
    position: absolute;
    display: flex;
    align-items: center;
    gap: 10px;
  }
  .wordmark__square {
    background: var(--navy);
    flex: none;
  }
  .wordmark__text {
    color: var(--navy);
    font-weight: 400;
    line-height: 1;
    text-transform: uppercase;
  }
  .wordmark__text span { display: block; }
  .wordmark__sub { letter-spacing: 0.22em; text-align: right; margin-top: 4px; }

  /* Business card front */
  .card-front { left: 68px; top: 78px; width: 344px; height: 205px; }
  .card-front .wordmark { left: 16px; top: 73px; }
  .card-front .wordmark__square { width: 44px; height: 44px; }
  .card-front .wordmark__name { font-size: 26px; }
  .card-front .wordmark__sub { font-size: 12px; }

  /* Business card back */
  .card-back { left: 789px; top: 78px; width: 344px; height: 205px; }
  .card-back .wordmark { left: 12px; top: 12px; gap: 6px; }
  .card-back .wordmark__square { width: 22px; height: 22px; }
  .card-back .wordmark__name { font-size: 13px; }
  .card-back .wordmark__sub { font-size: 6.5px; margin-top: 2px; }
  .card-back__person {
    position: absolute;
    left: 0; right: 0; top: 62px;
    text-align: center;
  }
  .card-back__name {
    font-size: 28px;
    letter-spacing: 0.03em;
    color: var(--navy);
    margin: 0;
    font-weight: 400;
  }
  .card-back__role {
    font-size: 16px;
    color: var(--plum);
    margin: 2px 0 0;
  }
  .card-back__address,
  .card-back__contact {
    position: absolute;
    bottom: 10px;
    font-size: 8px;
    line-height: 10px;
    font-style: normal;
  }
  .card-back__address { left: 12px; }
  .card-back__contact { right: 12px; text-align: right; }

  /* Envelope */
  .envelope { left: 274px; top: 347px; width: 652px; height: 335px; box-shadow: none; }
  .envelope__frame { position: absolute; inset: 0; }
  .envelope .wordmark { left: 205px; top: 21px; gap: 8px; }
  .envelope .wordmark__square { width: 40px; height: 40px; }
  .envelope .wordmark__name { font-size: 23px; }
  .envelope .wordmark__sub { font-size: 10px; }
  .envelope__address {
    position: absolute;
    left: 0; right: 0; top: 77px;
    text-align: center;
    font-size: 7.5px;
    line-height: 9.5px;
    font-style: normal;
  }
</style>
</head>
<body>

  <section class="sheet card-front" aria-label="Business card, front">
    <div class="wordmark">
      <div class="wordmark__square"></div>
      <div class="wordmark__text">
        <span class="wordmark__name">Marcus Fenwell</span>
        <span class="wordmark__sub">Accountants</span>
      </div>
    </div>
  </section>

  <section class="sheet card-back" aria-label="Business card, back">
    <div class="wordmark">
      <div class="wordmark__square"></div>
      <div class="wordmark__text">
        <span class="wordmark__name">Marcus Fenwell</span>
        <span class="wordmark__sub">Accountants</span>
      </div>
    </div>
    <div class="card-back__person">
      <h1 class="card-back__name">OLIVER HART</h1>
      <p class="card-back__role">Manager</p>
    </div>
    <address class="card-back__address">
      12 Linden Court<br>
      Alderway Business Park<br>
      Kestrel Road<br>
      Ashbury-on-the-Green,<br>
      Middlesex, HA4 2LP
    </address>
    <address class="card-back__contact">
      Tel: 020 7946 0321<br>
      mail@marcusfenwell.co.uk
    </address>
  </section>

  <section class="sheet envelope" aria-label="Envelope">
    <svg class="envelope__frame" width="652" height="335" viewBox="0 0 652 335" aria-hidden="true">
      <rect x="4.5" y="4.5" width="643" height="326" fill="#fff" stroke="var(--envelope-edge)" stroke-width="9"/>
      <polyline points="9,9 324,223 643,9" fill="none" stroke="var(--envelope-edge)" stroke-width="7"/>
      <line x1="9" y1="326" x2="256" y2="173" stroke="var(--envelope-edge)" stroke-width="7"/>
      <line x1="643" y1="326" x2="394" y2="173" stroke="var(--envelope-edge)" stroke-width="7"/>
    </svg>
    <div class="wordmark">
      <div class="wordmark__square"></div>
      <div class="wordmark__text">
        <span class="wordmark__name">Marcus Fenwell</span>
        <span class="wordmark__sub">Accountants</span>
      </div>
    </div>
    <address class="envelope__address">
      12 Linden Court, Alderway Business Park, Kestrel Road,<br>
      Ashbury-on-the-Green, Middlesex, HA4 2LP<br>
      Tel: 020 7946 0321<br>
      www.marcusfenwell.co.uk
    </address>
  </section>

</body>
</html>
```